Poster for Billard- & Sportsbar: "Specials"

Hi,
I Need a Poster for my Billard- & Sportsbar, which Shows our weekly Specials.
The size should be DinA0 (84 x 118.8 cm). Please notice the print instructions attached.

Text Information for the Poster:

"Wochenhighlights

Dienstag: Flatrate-Billard
Für nur 5€ (7€) pro Person den ganzen Abend Pool-Billard (Snooker)spielen

Mittwoch: Studenten-Nacht
Studenten & Auszubildende spielen Pool-Billard für nur 4,50€ die Stunde

Donnerstag: Snooker-Donnerstag
Donnerstags kostet der Snooker Tisch gerade mal 5€ die Stunde

Freitag: Talwinkel-Special
6 Falk Talwinkel-Pils für nur 11,99€

Samstag: Schau dein Wunschsspiel
Reserviere die Private Lounge und schaue das Adlerliga-Spiel deiner Wahl. Reservierungsgebühr: 10€, ab 6 Personen kostenlos.
(Gilt auch für WK, NSV-Pokal & Englische Wochen)

Sonntag: Play for Free
Wer vor 18:00 Uhr mit dem Spielen beginnt, spielt den ganzen Abend umsonst!"

You can choose the Colors free. If you use Pictures, take care that they are free or send me the link where they can get bought.

I have uploaded the logo of my bar. You can use it in the poster, but please not too big.

You can maybe use the Colors of the logo as main Colors. But it is not a must.

If you have questions, just contact me!

Thank you in advance!

Tobias

A short update: Please mind, that it is the most important Thing, that the customers can read the Special offers! Thank you

```html
<!DOCTYPE html>
<html lang="de">
<head>
<meta charset="utf-8">
<title>Kugelwerk – Wochenhighlights</title>
<link rel="stylesheet" href="https://fonts.googleapis.com/css2?family=Archivo+Black&family=Roboto+Condensed:ital,wght@0,400;0,700;0,900;1,300;1,400&display=swap">
<style>
  :root {
    --green: #23a049;
    --green-deep: #1a8a3e;
    --green-dark: #13702f;
    --ink: #0b1f12;
    --label-ink: #12612c;
    --white: #ffffff;
    --placeholder: rgba(255, 255, 255, 0.14);
    --placeholder-dark: rgba(0, 0, 0, 0.10);
  }
  html, body {
    margin: 0;
    padding: 0;
    overflow: hidden;
  }
  .poster {
    position: relative;
    width: 849px;
    height: 1200px;
    overflow: hidden;
    background: linear-gradient(180deg, var(--green) 0%, var(--green) 55%, var(--green-deep) 80%, var(--green-dark) 100%);
    font-family: "Roboto Condensed", sans-serif;
    color: var(--white);
  }
  .poster__backdrop {
    position: absolute;
    left: 0; right: 0; top: 650px; bottom: 0;
    background: linear-gradient(180deg, rgba(255,255,255,0.04), var(--placeholder-dark));
  }
  .brand {
    position: absolute;
    top: 24px;
    left: 0; right: 0;
    text-align: center;
  }
  .brand__name {
    font-weight: 900;
    font-size: 64px;
    line-height: 1;
    letter-spacing: 1px;
    color: var(--ink);
  }
  .brand__tagline {
    margin-top: 4px;
    padding-left: 180px;
    font-size: 9px;
    font-weight: 700;
    letter-spacing: 1px;
    color: var(--ink);
  }
  .title {
    position: absolute;
    top: 124px;
    left: 0; right: 0;
    margin: 0;
    text-align: center;
    font-style: italic;
    font-weight: 400;
    font-size: 90px;
    line-height: 1;
    letter-spacing: 0;
  }
  .illustration {
    position: absolute;
    background: var(--placeholder);
    border-radius: 4px;
  }
  .illustration--cue { left: 69px; top: 222px; width: 711px; height: 16px; }
  .illustration--balls-rack { left: 584px; top: 258px; width: 204px; height: 90px; }
  .illustration--three-balls { left: 708px; top: 530px; width: 86px; height: 80px; }
  .illustration--two-balls { left: 732px; top: 690px; width: 62px; height: 100px; }
  .illustration--two-balls-low { left: 722px; top: 886px; width: 66px; height: 102px; }
  .illustration--snooker-reds { left: 74px; top: 1074px; width: 124px; height: 86px; }
  .day {
    position: absolute;
    left: 0;
    width: 100%;
  }
  .day__label {
    position: absolute;
    left: 0;
    top: 0;
    width: 201px;
    height: 36px;
    background: var(--white);
    color: var(--label-ink);
    font-family: "Archivo Black", sans-serif;
    font-size: 20px;
    line-height: 36px;
    padding-left: 30px;
    box-sizing: border-box;
    letter-spacing: 1px;
  }
  .day__label--wide { width: 226px; }
  .day__heading {
    position: absolute;
    left: 246px;
    top: -3px;
    margin: 0;
    font-style: italic;
    font-weight: 400;
    font-size: 36px;
    line-height: 42px;
    white-space: nowrap;
  }
  .day__text {
    position: absolute;
    left: 246px;
    top: 42px;
    margin: 0;
    font-size: 27px;
    line-height: 27px;
    white-space: nowrap;
  }
  .day__note { font-size: 20px; line-height: 34px; }
</style>
</head>
<body>
<main class="poster">
  <div class="poster__backdrop" role="img" aria-label="Faint photo of a billiard table in the bar"></div>

  <header class="brand">
    <div class="brand__name">KUGELWERK</div>
    <div class="brand__tagline">BILLARD · SPORTSBAR · LOUNGE</div>
  </header>

  <h1 class="title">WOCHENHIGHLIGHTS</h1>
  <div class="illustration illustration--cue" role="img" aria-label="Billiard cue illustration"></div>
  <div class="illustration illustration--balls-rack" role="img" aria-label="Pool balls beside a wooden triangle rack"></div>

  <section class="day" style="top:299px">
    <div class="day__label">DIENSTAG</div>
    <h2 class="day__heading">Flatrate-Billard</h2>
    <p class="day__text">Für nur 5€ (7€) pro Person<br>den ganzen Abend Pool-Billard (Snooker)spielen</p>
  </section>

  <section class="day" style="top:435px">
    <div class="day__label">MITTWOCH</div>
    <h2 class="day__heading">Studenten-Nacht</h2>
    <p class="day__text">Studenten &amp; Auszubildende spielen Pool-Billard<br>für nur 4,50€ die Stunde</p>
  </section>

  <div class="illustration illustration--three-balls" role="img" aria-label="Three pool balls"></div>

  <section class="day" style="top:564px">
    <div class="day__label day__label--wide">DONNERSTAG</div>
    <h2 class="day__heading">Snooker-Donnerstag</h2>
    <p class="day__text">Donnerstags kostet der Snooker Tisch<br>gerade mal 5€ die Stunde</p>
  </section>

  <section class="day" style="top:698px">
    <div class="day__label">FREITAG</div>
    <h2 class="day__heading">Talwinkel-Special</h2>
    <p class="day__text">6 Falk Talwinkel-Pils für nur 11,99€</p>
  </section>

  <div class="illustration illustration--two-balls" role="img" aria-label="Two pool balls"></div>

  <section class="day" style="top:801px">
    <div class="day__label">SAMSTAG</div>
    <h2 class="day__heading">Schau dein Wunschsspiel</h2>
    <p class="day__text">Reserviere die Private Lounge und schaue<br>das Adlerliga-Spiel deiner Wahl.<br>Reservierungsgebühr: 10€,<br>ab 6 Personen kostenlos.<br><span class="day__note">(Gilt auch für WK, NSV-Pokal &amp; Englische Wochen)</span></p>
  </section>

  <div class="illustration illustration--two-balls-low" role="img" aria-label="Pool ball and white cue ball"></div>

  <section class="day" style="top:1016px">
    <div class="day__label">SONNTAG</div>
    <h2 class="day__heading">Play for Free</h2>
    <p class="day__text">Wer vor 18:00 Uhr mit dem Spielen beginnt,<br>spielt den ganzen Abend umsonst!</p>
  </section>

  <div class="illustration illustration--snooker-reds" role="img" aria-label="Triangle of red snooker balls"></div>
</main>
</body>
</html>
```